Business Card Design Project

A double sided business card for presentation to business leaders in corporate.

Target Market(s)

Corporate, business professionals, HR

Industry/Entity Type

Business

Requirements
Must have
• FRONT

Logo

www.brightlanecoaching.com.au

BACK

Mara Pollen-Drew
Director

+ 61 (0) 418 536 204
mara@brightlanecoaching.com.au
www.brightlanecoaching.com.au

Growth through energy and employee engagement

("ripples" of logo, bottom corner)

Must be:
- double sided
size: 86 x 54mm
supplied as one pdf with crop marks shown (+- 1mm, with 2-3 mm bleed)

```html
<!DOCTYPE html>
<html lang="en">
<head>
<meta charset="utf-8">
<title>Bright Lane Coaching – Business Card</title>
<link rel="stylesheet" href="https://fonts.googleapis.com/css2?family=Ubuntu:wght@400;500;700&display=swap">
<style>
  :root {
    --stage: #d4d4d6;
    --card-light: #f1f1f2;
    --card-mid: #d9d9db;
    --ripple-tone: #e3e3e5;
    --bubble: #3a3a3c;
    --bubble-edge: #ffffff;
    --plum: #7b2a6c;
    --ink: #2c2c2e;
    --text-light: #ffffff;
  }
  * { box-sizing: border-box; margin: 0; padding: 0; }
  html, body { width: 1200px; height: 861px; overflow: hidden; }
  body {
    background: var(--stage);
    font-family: "Ubuntu", sans-serif;
    color: var(--ink);
    position: relative;
  }
  .card {
    position: absolute;
    top: 267px;
    width: 520px;
    height: 327px;
    border-radius: 18px;
    background: linear-gradient(160deg, var(--card-light) 0%, var(--card-mid) 100%);
    overflow: hidden;
    box-shadow: 0 6px 18px rgba(0,0,0,0.18);
  }
  .card--front { left: 50px; }
  .card--back { left: 630px; }

  .ripple-field {
    position: absolute;
    inset: 0;
    background: radial-gradient(circle at 20% 80%, var(--ripple-tone) 0%, transparent 60%),
                radial-gradient(circle at 85% 20%, var(--ripple-tone) 0%, transparent 55%);
    opacity: 0.8;
  }

  .bubble { position: absolute; }
  .bubble svg { position: absolute; inset: 0; overflow: visible; }
  .bubble__text { position: absolute; color: var(--text-light); white-space: nowrap; }

  /* Front */
  .card--front .bubble { left: 205px; top: 45px; width: 330px; height: 135px; }
  .card--front .bubble__text {
    left: 24px; top: 34px;
    font-weight: 700; font-size: 17.5px; letter-spacing: 0.3px;
  }
  .wordmark {
    position: absolute;
    color: var(--plum);
    font-weight: 500;
    line-height: 0.95;
    display: flex;
    align-items: center;
    gap: 14px;
  }
  .wordmark__dot {
    border-radius: 50%;
    background: var(--plum);
    flex: none;
  }
  .card--front .wordmark { left: 34px; top: 190px; font-size: 46px; }
  .card--front .wordmark__dot { width: 22px; height: 22px; }

  /* Back */
  .card--back .bubble { left: 285px; top: 48px; width: 250px; height: 120px; }
  .name {
    left: 22px; top: 18px;
    font-weight: 700; font-size: 22px;
  }
  .role {
    left: 22px; top: 47px;
    font-size: 14px;
  }
  .card--back .wordmark { left: 26px; top: 62px; font-size: 31px; gap: 10px; }
  .card--back .wordmark__dot { width: 14px; height: 14px; }
  .tagline {
    position: absolute;
    left: 36px; top: 204px; width: 230px;
    text-align: center;
    font-weight: 500; font-size: 13.5px; line-height: 1.5;
  }
  .contacts {
    position: absolute;
    left: 276px; top: 194px;
    list-style: none;
    font-size: 12.5px;
  }
  .contacts li {
    display: flex; align-items: center; gap: 7px;
    height: 29px;
    white-space: nowrap;
  }
  .contacts svg { width: 19px; height: 19px; flex: none; }
</style>
</head>
<body>

<section class="card card--front" aria-label="Card front">
  <div class="ripple-field" role="img" aria-label="Faint repeating ripple pattern across the card"></div>
  <div class="bubble">
    <svg viewBox="0 0 330 135" width="330" height="135">
      <path d="M14 20 Q14 4 30 6 L330 22 L330 100 L110 94 L66 128 L72 92 L30 92 Q14 92 14 76 Z"
            fill="var(--bubble)" stroke="var(--bubble-edge)" stroke-width="4" stroke-linejoin="round"/>
    </svg>
    <p class="bubble__text">www.brightlanecoaching.com.au</p>
  </div>
  <div class="wordmark">
    <span class="wordmark__dot"></span>
    <span>bright lane<br>coaching</span>
  </div>
</section>

<section class="card card--back" aria-label="Card back">
  <div class="ripple-field" role="img" aria-label="Faint repeating ripple pattern across the card"></div>
  <div class="bubble">
    <svg viewBox="0 0 250 120" width="250" height="120">
      <path d="M10 16 Q10 2 24 4 L250 16 L250 84 L110 80 L74 112 L76 78 L24 76 Q10 76 10 62 Z"
            fill="var(--bubble)" stroke="var(--bubble-edge)" stroke-width="4" stroke-linejoin="round"/>
    </svg>
    <p class="bubble__text name">Mara Pollen-Drew</p>
    <p class="bubble__text role">Director</p>
  </div>
  <div class="wordmark">
    <span class="wordmark__dot"></span>
    <span>bright lane<br>coaching</span>
  </div>
  <p class="tagline">Growth through energy and employee engagement</p>
  <ul class="contacts">
    <li>
      <svg viewBox="0 0 20 20" aria-hidden="true">
        <circle cx="10" cy="10" r="9" fill="none" stroke="var(--ink)" stroke-width="1.5"/>
        <rect x="7" y="4.5" width="6" height="11" rx="1.2" fill="var(--ink)"/>
        <rect x="8.2" y="6" width="3.6" height="4" fill="#fff"/>
      </svg>
      <span>+ 61 (0) 418 536 204</span>
    </li>
    <li>
      <svg viewBox="0 0 20 20" aria-hidden="true">
        <circle cx="10" cy="10" r="9" fill="none" stroke="var(--ink)" stroke-width="1.5"/>
        <rect x="4.5" y="6.5" width="11" height="7.5" fill="var(--ink)"/>
        <path d="M4.8 6.8 L10 11 L15.2 6.8" fill="none" stroke="#fff" stroke-width="1"/>
      </svg>
      <span>mara@brightlanecoaching.com.au</span>
    </li>
    <li>
      <svg viewBox="0 0 20 20" aria-hidden="true">
        <circle cx="10" cy="10" r="9" fill="none" stroke="var(--ink)" stroke-width="1.5"/>
        <rect x="4.5" y="5" width="11" height="8" fill="var(--ink)"/>
        <rect x="6" y="6.5" width="8" height="5" fill="#fff"/>
        <rect x="8" y="13" width="4" height="2" fill="var(--ink)"/>
      </svg>
      <span>www.brightlanecoaching.com.au</span>
    </li>
  </ul>
</section>

</body>
</html>
```